Business Card and stationary project for Nutrition Consulitng Company
QV Nutrition Consulting, PC
Business Card and stationary project for Nutrition Consulitng Company - Health
Creative Brief
Bright & Fun-filled
leave adjustable for each staff
5182 27th Ave. Suite 100 Columbus, NE 68457
leave adjustable
rmalden@qvnutritionconsulting.example
www.qvnutritionconsulting.example
I would like the business cards to be editable for each staff member. This would include name, title, cell number, and email address.
please address my website www.qvnutriitionconsulting.example for ideas, as well as the uploaded logo and letter head

```html
<!DOCTYPE html>
<html lang="en">
<head>
<meta charset="utf-8">
<title>Brightfield Nutrition Consulting, PC — Business Card</title>
<link rel="stylesheet" href="https://fonts.googleapis.com/css2?family=Open+Sans:wght@400;600;700&display=swap">
<style>
  :root {
    --bg: #ecebe8;
    --card-white: #ffffff;
    --brown: #7a4a2a;
    --brown-dark: #5a3419;
    --brown-back: #7d4c2c;
    --orange: #e9762b;
    --orange-light: #f3a35a;
    --ring-green: #9cbf3b;
    --ring-red: #c8312f;
    --ring-yellow: #f2c33a;
    --text-light: #f4e8dc;
    --shadow: rgba(40, 25, 10, 0.25);
  }
  * { box-sizing: border-box; margin: 0; padding: 0; }
  html, body { width: 1200px; height: 600px; overflow: hidden; }
  body {
    background: var(--bg);
    font-family: "Open Sans", Arial, sans-serif;
    position: relative;
  }
  .card {
    position: absolute;
    top: 140px;
    width: 520px;
    height: 300px;
    border-radius: 14px;
    overflow: hidden;
    box-shadow: 0 6px 18px var(--shadow);
  }
  .card--front { left: 50px; background: var(--card-white); }
  .card--back  { left: 630px; background: var(--brown-back); }

  .front-waves { position: absolute; inset: 0; width: 100%; height: 100%; }

  .brand {
    position: absolute;
    top: 30px;
    left: 150px;
    width: 350px;
    text-align: center;
  }
  .brand__name {
    font-weight: 700;
    font-size: 18px;
    letter-spacing: 0.2px;
    color: var(--brown-dark);
    line-height: 1.15;
    white-space: nowrap;
  }
  .brand__tagline {
    margin-top: 5px;
    font-size: 7.5px;
    font-weight: 600;
    color: var(--orange);
    white-space: nowrap;
  }

  .person { position: absolute; top: 102px; left: 118px; color: var(--brown-dark); }
  .person__name { font-size: 20px; font-weight: 400; line-height: 1.1; }
  .person__title { font-size: 9px; margin-top: 2px; }

  .rings {
    position: absolute;
    border-radius: 50%;
    background: radial-gradient(circle at 40% 40%, var(--ring-yellow) 0%, var(--ring-green) 35%, var(--orange) 65%, var(--ring-red) 100%);
  }
  .card--front .rings { left: 42px; top: 172px; width: 104px; height: 104px; }

  .address {
    position: absolute;
    left: 192px;
    top: 232px;
    font-size: 8px;
    font-style: normal;
    line-height: 1.45;
    color: var(--text-light);
    white-space: nowrap;
  }
  .contact {
    position: absolute;
    left: 312px;
    top: 190px;
    list-style: none;
    font-size: 8px;
    line-height: 1.55;
    color: var(--text-light);
    white-space: nowrap;
  }
  .contact li { display: flex; align-items: center; gap: 5px; }
  .contact svg { width: 8px; height: 8px; flex: none; }

  .card--back .rings--faint {
    left: 150px; top: 60px; width: 180px; height: 180px; opacity: 0.28;
    background: radial-gradient(circle, var(--orange-light) 0%, var(--ring-red) 60%, var(--brown-back) 100%);
  }
  .card--back .rings--bright { left: 232px; top: 44px; width: 108px; height: 108px; }
  .back-url {
    position: absolute;
    left: 154px;
    top: 214px;
    font-size: 8.5px;
    color: var(--ring-green);
    white-space: nowrap;
  }
</style>
</head>
<body>
  <section class="card card--front">
    <svg class="front-waves" viewBox="0 0 520 300" preserveAspectRatio="none" aria-hidden="true">
      <path d="M0 178 C140 150 300 150 520 92 L520 300 L0 300 Z" fill="#e9762b"/>
      <path d="M0 190 C150 160 310 158 520 104 L520 300 L0 300 Z" fill="#7a4a2a"/>
    </svg>

    <div class="brand">
      <p class="brand__name">Brightfield Nutrition Consulting, PC</p>
      <p class="brand__tagline">Helping You Eat Well Through Every Stage of Life</p>
    </div>

    <div class="person">
      <p class="person__name">Your name</p>
      <p class="person__title">Your title</p>
    </div>

    <div class="rings" role="img" aria-label="Cluster of colourful overlapping rings in green, red, yellow and orange"></div>

    <address class="address">
      5182 27th Ave. Unit 4<br>
      Millbrook, KS 67512
    </address>

    <ul class="contact">
      <li><svg viewBox="0 0 10 10"><path d="M2 1l2 2-1 1c.6 1.3 1.7 2.4 3 3l1-1 2 2-1.5 1.5C4 9 1 6 .5 2.5z" fill="#f4e8dc"/></svg>402-555-0142</li>
      <li><svg viewBox="0 0 10 10"><path d="M2 1l2 2-1 1c.6 1.3 1.7 2.4 3 3l1-1 2 2-1.5 1.5C4 9 1 6 .5 2.5z" fill="#f4e8dc"/></svg>402-555-0177</li>
      <li><svg viewBox="0 0 10 10"><rect x="1" y="2" width="8" height="6" fill="none" stroke="#f4e8dc"/><path d="M1 2l4 3 4-3" fill="none" stroke="#f4e8dc"/></svg>402-555-0190</li>
      <li><svg viewBox="0 0 10 10"><rect x="1" y="2" width="8" height="6" fill="none" stroke="#f4e8dc"/><path d="M1 2l4 3 4-3" fill="none" stroke="#f4e8dc"/></svg>rmalden@qvnutritionconsulting.example</li>
      <li><svg viewBox="0 0 10 10"><circle cx="5" cy="5" r="4" fill="none" stroke="#f4e8dc"/><path d="M1 5h8M5 1c2 2 2 6 0 8M5 1c-2 2-2 6 0 8" fill="none" stroke="#f4e8dc" stroke-width=".7"/></svg>www.qvnutritionconsulting.example</li>
    </ul>
  </section>

  <section class="card card--back">
    <div class="rings rings--faint" role="img" aria-label="Large faint rings decoration in warm red and orange tones"></div>
    <div class="rings rings--bright" role="img" aria-label="Cluster of colourful overlapping rings in green, red, yellow and orange"></div>
    <p class="back-url">www.qvnutritionconsulting.example</p>
  </section>
</body>
</html>
```